IT services company needs a business card designed

-2 sided business card.-Front is going to be the logo raised (3D floating effect) on a black background. Make the logos spider web shiny silver and keep the spider the same design. -Back needs to have the following information:Darrel Sotho, Managing Partner, Cell: 738-402-1954, Website: Plankhorn.com, Email: Darrel@Plankhorn.com
Target Market(s)
IT Services
Industry/Entity Type
It Company
Contact Information for Business Card
-2 sided business card.
-Front is going to be the logo raised (3D floating effect) on a black background. Make the logos spider web shiny silver and keep the spider the same design.
-Back needs to have the following information:
Darrel Sotho, Managing Partner, Cell: 738-402-1954, Website: Plankhorn.com, Email: Darrel@Plankhorn.com

```html
<!DOCTYPE html>
<html lang="en">
<head>
<meta charset="utf-8">
<title>Plankhorn Business Card</title>
<link rel="stylesheet" href="https://fonts.googleapis.com/css2?family=Mulish:wght@300;400&display=swap">
<style>
  :root {
    --backdrop: #5a5c5f;
    --card-dark: #1f1f20;
    --card-light: #ffffff;
    --accent: #1aa3e8;
    --ink: #3a4350;
    --rule: #4a4a4a;
    --white: #ffffff;
  }
  * { margin: 0; padding: 0; box-sizing: border-box; }
  html, body {
    width: 1200px; height: 899px; overflow: hidden;
    background: var(--backdrop);
    font-family: "Mulish", Arial, sans-serif;
  }
  .card {
    position: absolute; left: 320px;
    width: 560px; height: 320px;
    border-radius: 22px;
    overflow: hidden;
  }
  .card-front { top: 60px; background: var(--card-dark); }
  .card-back { top: 420px; background: var(--card-light); }

  .front-wordmark {
    position: absolute; left: 0; right: 0; top: 128px;
    display: flex; align-items: center; justify-content: center; gap: 14px;
  }
  .wordmark-text {
    color: var(--white); font-weight: 300;
    font-size: 46px; letter-spacing: 3px;
  }
  .wordmark-dot {
    width: 12px; height: 12px; border-radius: 50%;
    background: var(--accent);
  }

  .back-logo {
    position: absolute; left: 40px; top: 70px;
    display: flex; align-items: center; gap: 10px;
  }
  .back-logo .wordmark-text { color: var(--accent); font-size: 30px; letter-spacing: 2px; }
  .back-logo .wordmark-dot { width: 9px; height: 9px; }

  .person {
    position: absolute; right: 36px; top: 118px; text-align: right;
  }
  .person-name {
    color: var(--accent); font-weight: 300; font-size: 30px; letter-spacing: 1px;
    text-transform: uppercase; line-height: 1;
  }
  .person-title {
    color: var(--ink); font-size: 14px; letter-spacing: 1.5px; margin-top: 6px;
  }
  .divider {
    position: absolute; left: 30px; right: 30px; top: 200px;
    border-top: 1px solid var(--rule);
  }
  .contacts {
    position: absolute; left: 36px; top: 220px;
    list-style: none;
  }
  .contacts li {
    display: flex; align-items: center; gap: 10px;
    color: var(--ink); font-size: 15px; letter-spacing: 1px; line-height: 26px;
  }
  .contacts svg { width: 14px; height: 14px; fill: var(--accent); flex: none; }
</style>
</head>
<body>
  <section class="card card-front" aria-label="Card front">
    <div class="front-wordmark">
      <span class="wordmark-text">PLANKHORN</span>
      <span class="wordmark-dot"></span>
    </div>
  </section>

  <section class="card card-back" aria-label="Card back">
    <div class="back-logo">
      <span class="wordmark-text">PLANKHORN</span>
      <span class="wordmark-dot"></span>
    </div>

    <div class="person">
      <p class="person-name">Darrel Sotho</p>
      <p class="person-title">Managing Partner</p>
    </div>

    <div class="divider"></div>

    <ul class="contacts">
      <li>
        <svg viewBox="0 0 24 24" aria-hidden="true"><path d="M6.6 10.8a15.1 15.1 0 0 0 6.6 6.6l2.2-2.2c.3-.3.7-.4 1-.2 1.1.4 2.3.6 3.6.6.6 0 1 .4 1 1V20c0 .6-.4 1-1 1A17 17 0 0 1 3 4c0-.6.4-1 1-1h3.5c.6 0 1 .4 1 1 0 1.3.2 2.5.6 3.6.1.3 0 .7-.2 1z"/></svg>
        738-402-1954
      </li>
      <li>
        <svg viewBox="0 0 24 24" aria-hidden="true"><path d="M2 5h20v14H2z M2 5l10 8 10-8" /></svg>
        Darrel@Plankhorn.com
      </li>
      <li>
        <svg viewBox="0 0 24 24" aria-hidden="true"><circle cx="12" cy="12" r="10"/></svg>
        www.Plankhorn.com
      </li>
    </ul>
  </section>
</body>
</html>
```